Awesome photographers card for an awesome new business

Double sided business card Black background and silver logo in middle on one side. Details on otherside. please keep it simple

Photographer

Gavin Tolley
0482615073
GavinTolleyPhotography82@lumenpost.com
www.GavinTolleyPhotography.com.au
Instagram _Gavin_tolley

Requirements
Must have
• My logo in Silver
• please use instagram logo instead of "Instagram"

```html
<!DOCTYPE html>
<html lang="en">
<head>
<meta charset="utf-8">
<title>Gavin Tolley Photography – Business Card</title>
<link rel="stylesheet" href="https://fonts.googleapis.com/css2?family=Open+Sans:wght@400;700&display=swap">
<style>
  :root {
    --backdrop: #2a2a2a;
    --paper: #f7f7f7;
    --ink-black: #111111;
    --silver-light: #e6e6e6;
    --silver-mid: #b9b9b9;
    --silver-dark: #8e8e8e;
    --text-dark: #2a2a2a;
    --text-grey: #6d6d6d;
  }
  * { box-sizing: border-box; margin: 0; padding: 0; }
  html, body { width: 1200px; height: 900px; overflow: hidden; }
  body {
    background: var(--backdrop);
    font-family: "Open Sans", Arial, sans-serif;
    display: flex;
    flex-direction: column;
    align-items: center;
    justify-content: center;
    gap: 48px;
  }
  .card {
    position: relative;
    width: 660px;
    height: 377px;
    border-radius: 4px;
    overflow: hidden;
    box-shadow: 0 10px 30px rgba(0,0,0,.45);
  }

  /* Front */
  .card-front { background: var(--paper); }
  .front-brand {
    position: absolute;
    top: 120px; left: 0; right: 0;
    display: flex; align-items: center; justify-content: center; gap: 16px;
    font-size: 40px; font-weight: 400; color: var(--silver-dark);
    letter-spacing: 1px;
  }
  .front-brand .brand-dot {
    width: 22px; height: 22px; border-radius: 50%;
    background: var(--silver-mid);
  }
  .front-url {
    position: absolute;
    left: 40px; bottom: 40px;
    font-size: 15px; letter-spacing: 3px; color: var(--text-grey);
  }

  /* Back */
  .card-back { background: linear-gradient(180deg, var(--silver-light) 0%, var(--silver-mid) 70%, var(--silver-dark) 100%); }
  .back-band { position: absolute; inset: 0; width: 100%; height: 100%; }
  .back-emblem {
    position: absolute;
    top: 62px; left: 50%;
    transform: translateX(-50%);
    width: 132px; height: 132px;
    border-radius: 50%;
    border: 3px solid var(--silver-light);
    background: var(--ink-black);
    display: flex; align-items: center; justify-content: center;
    text-align: center;
    font-size: 17px; line-height: 1.25; color: var(--silver-light);
  }
  .contact {
    position: absolute;
    top: 218px; left: 0; right: 0;
    text-align: center;
    color: var(--text-dark);
    font-size: 15px; line-height: 1.3;
  }
  .contact-name {
    font-weight: 700; font-size: 19px; letter-spacing: .5px;
    text-transform: uppercase; margin-bottom: 4px;
  }
  .contact-social { display: inline-flex; align-items: center; gap: 6px; }
  .contact-social .social-square {
    width: 12px; height: 12px; background: var(--text-dark); border-radius: 2px;
  }
</style>
</head>
<body>
  <section class="card card-front">
    <div class="front-brand"><span class="brand-dot"></span>Gavin Tolley</div>
    <p class="front-url">www.GavinTolleyPhotography.com.au</p>
  </section>

  <section class="card card-back">
    <svg class="back-band" viewBox="0 0 660 377" preserveAspectRatio="none" aria-hidden="true">
      <path d="M0 0 H660 V150 Q330 230 0 175 Z" fill="#111111"/>
      <path d="M0 175 Q330 230 660 150" fill="none" stroke="#d4d4d4" stroke-width="4"/>
    </svg>
    <div class="back-emblem">Gavin<br>Tolley</div>
    <div class="contact">
      <p class="contact-name">Gavin Tolley</p>
      <p>(P) 0482615073</p>
      <p>GavinTolleyPhotography82@lumenpost.com</p>
      <p>www.GavinTolleyPhotography.com.au</p>
      <p class="contact-social"><span class="social-square"></span>_Gavin_tolley</p>
    </div>
  </section>
</body>
</html>
```